Design Android App for Creating Estimates and Invoices

This project is to create a graphic design for an Android mobile app called Velmira Builder App which is an app that will help contractors to quickly create professional estimates and invoices, accept payments, manage clients and projects and run their business smoothly.

Link to some designs I created myself, hoping to get even better design from you
https://snapvault.example/album/qTrWpe

This project is similar to
https://appmarket.example/store/apps/details?id=com.brevlo.android.brevlo
https://appmarket.example/store/apps/details?id=com.tuvrq.quikbill

Check this Google Doc for more information. http://shrtn.example/8KmPqX4

Target Market(s)

Contractors, Home Improvement Professionals, Home Builders,

Industry/Entity Type

Residential Construction

Requirements
Must have
• Non-cluttered screen for Estimates, Enough white space between fields.
Nice to have
• Be different from the two example designs shown

```html
<!DOCTYPE html>
<html lang="en">
<head>
<meta charset="utf-8">
<title>Velmira Builder App – Onboarding Screens</title>
<link href="https://fonts.googleapis.com/css2?family=Poppins:wght@400;500;600&display=swap" rel="stylesheet">
<style>
  :root{
    --bg-deep:#34529a;
    --bg-light:#4c6db3;
    --screen:#f7f7f7;
    --brand-blue:#1f6db5;
    --brand-orange:#f7931e;
    --button:#2f55a3;
    --ink:#1d1d1d;
    --muted:#777;
    --placeholder:#9a9a9a;
    --field-border:#dcdcdc;
    --white:#ffffff;
    --rule:rgba(255,255,255,.35);
  }
  *{box-sizing:border-box;margin:0;padding:0}
  html,body{width:1200px;height:1200px;overflow:hidden}
  body{
    position:relative;
    font-family:"Poppins",sans-serif;
    background:radial-gradient(circle at 30% 20%,var(--bg-light),var(--bg-deep) 75%);
    color:var(--ink);
  }
  .abs{position:absolute}

  /* header brand */
  .brand-mark{left:358px;top:30px;width:100px;height:100px;border-radius:50%;background:var(--brand-orange)}
  .brand-name{left:486px;top:44px;color:var(--white);font-weight:600;line-height:1}
  .brand-name .line1{display:block;font-size:44px;letter-spacing:5px}
  .brand-name .line2{display:block;font-size:16px;letter-spacing:5.5px;margin-top:6px}

  /* screens */
  .screen{position:absolute;width:240px;height:522px;background:var(--screen);border-radius:22px;overflow:hidden}
  .screen.cut{height:480px;border-radius:22px 22px 0 0}
  .status{position:absolute;left:21px;top:8px;font-size:10px;color:#555}
  .status-icons{position:absolute;right:18px;top:10px;width:34px;height:8px}
  .home-bar{position:absolute;left:76px;top:508px;width:88px;height:3px;border-radius:2px;background:#c9c9c9}
  .back{position:absolute;left:8px;top:42px;width:18px;height:12px}

  .center{position:absolute;left:0;width:240px;text-align:center}
  .app-dot{position:absolute;border-radius:50%;background:var(--brand-orange)}
  .app-name{color:var(--brand-blue);font-weight:600;letter-spacing:2.5px}

  .title{font-size:15px;font-weight:500}
  .subtitle{font-size:10.5px;color:var(--muted);line-height:13px}

  .field{position:absolute;left:12px;width:216px;height:33px;background:var(--white);border:1px solid var(--field-border);border-radius:2px;font-size:10px;color:var(--placeholder);padding:0 11px;line-height:31px}
  .field.filled{color:var(--ink)}
  .field .caret{display:inline-block;width:1px;height:11px;background:var(--brand-orange);vertical-align:-1px}
  .field .dropdown{position:absolute;right:10px;top:14px;width:0;height:0;border-left:4px solid transparent;border-right:4px solid transparent;border-top:4px solid #666}

  .btn{position:absolute;left:34px;width:172px;height:33px;background:var(--button);border-radius:2px;color:var(--white);font-size:12px;font-weight:500;text-align:center;line-height:33px}
  .small{font-size:10.5px}
  .accent{color:var(--brand-orange);font-weight:500}

  .check{position:absolute;left:12px;top:283px;width:15px;height:15px;border:1px solid var(--button);border-radius:3px}
  .agree{position:absolute;left:37px;top:281px;font-size:10.5px;line-height:17px}

  /* labels */
  .rule{position:absolute;width:1px;background:var(--rule)}
  .label{position:absolute;color:var(--white);font-size:27px;font-weight:400;writing-mode:vertical-rl;transform:rotate(180deg);line-height:1}
</style>
</head>
<body>

  <!-- header brand -->
  <div class="abs brand-mark"></div>
  <div class="abs brand-name"><span class="line1">VELMIRA</span><span class="line2">BUILDER APP</span></div>

  <!-- Splash -->
  <section class="screen" style="left:69px;top:146px">
    <span class="status">9:41</span>
    <svg class="status-icons" viewBox="0 0 34 8"><rect x="0" y="5" width="2" height="3" fill="#777"/><rect x="3" y="3" width="2" height="5" fill="#777"/><rect x="6" y="1" width="2" height="7" fill="#777"/><rect x="22" y="1" width="11" height="6" rx="1" fill="#888"/></svg>
    <div class="app-dot" style="left:89px;top:206px;width:62px;height:62px"></div>
    <div class="center app-name" style="top:274px;font-size:27px">VELMIRA</div>
    <div class="center app-name" style="top:306px;font-size:10px;letter-spacing:3px">BUILDER APP</div>
    <div class="home-bar"></div>
  </section>

  <!-- Login -->
  <section class="screen" style="left:398px;top:222px">
    <span class="status">9:41</span>
    <svg class="status-icons" viewBox="0 0 34 8"><rect x="0" y="5" width="2" height="3" fill="#777"/><rect x="3" y="3" width="2" height="5" fill="#777"/><rect x="6" y="1" width="2" height="7" fill="#777"/><rect x="22" y="1" width="11" height="6" rx="1" fill="#888"/></svg>
    <div class="app-dot" style="left:95px;top:55px;width:50px;height:50px"></div>
    <div class="center app-name" style="top:110px;font-size:26px">VELMIRA</div>
    <div class="center title" style="top:178px">LOGIN</div>
    <div class="field" style="top:213px">Email</div>
    <div class="field" style="top:254px">Password</div>
    <div class="abs small" style="right:12px;top:295px">Forgot Password?</div>
    <div class="btn" style="top:329px">Let’s Go</div>
    <div class="center small" style="top:452px">Don’t have an account yet? <span class="accent">SignUp</span></div>
    <div class="home-bar"></div>
  </section>

  <!-- Signup 01 -->
  <section class="screen" style="left:728px;top:142px">
    <span class="status">9:41</span>
    <svg class="status-icons" viewBox="0 0 34 8"><rect x="0" y="5" width="2" height="3" fill="#777"/><rect x="3" y="3" width="2" height="5" fill="#777"/><rect x="6" y="1" width="2" height="7" fill="#777"/><rect x="22" y="1" width="11" height="6" rx="1" fill="#888"/></svg>
    <svg class="back" viewBox="0 0 18 12"><path d="M17 6H2M7 1 2 6l5 5" fill="none" stroke="#888" stroke-width="1.2"/></svg>
    <div class="center title" style="top:74px">Signup</div>
    <div class="center subtitle" style="top:108px">Please register to your Account to<br>continue with Velmira</div>
    <div class="field filled" style="top:149px">Dario<span class="caret"></span></div>
    <div class="field" style="top:190px">Email</div>
    <div class="field" style="top:232px">Industry<span class="dropdown"></span></div>
    <div class="check"><svg viewBox="0 0 15 15" width="13" height="13"><path d="M3.5 7.5l2.5 2.5 5-5.5" fill="none" stroke="#2f55a3" stroke-width="1.2"/></svg></div>
    <div class="agree">Agree to the <span class="accent">Privacy Policy</span> and<br><span class="accent">Terms &amp; Service</span></div>
    <div class="btn" style="top:336px">Next</div>
    <div class="center small" style="top:452px">Already have an account? <span class="accent">SignIn</span></div>
    <div class="home-bar"></div>
  </section>

  <!-- Signup 02 -->
  <section class="screen cut" style="left:923px;top:732px">
    <span class="status">9:41</span>
    <svg class="status-icons" viewBox="0 0 34 8"><rect x="0" y="5" width="2" height="3" fill="#777"/><rect x="3" y="3" width="2" height="5" fill="#777"/><rect x="6" y="1" width="2" height="7" fill="#777"/><rect x="22" y="1" width="11" height="6" rx="1" fill="#888"/></svg>
    <svg class="back" viewBox="0 0 18 12"><path d="M17 6H2M7 1 2 6l5 5" fill="none" stroke="#888" stroke-width="1.2"/></svg>
    <div class="center title" style="top:74px;font-weight:400">Hello <span style="font-weight:500">Dario!</span></div>
    <div class="center subtitle" style="top:108px">Enter your password below,<br>we’re just being extra careful</div>
    <div class="center title" style="top:166px">Set Password</div>
    <div class="field" style="top:202px">Password</div>
    <div class="field" style="top:242px">Confirm Password</div>
    <div class="btn" style="top:299px">Register Me</div>
  </section>

  <!-- labels -->
  <div class="rule" style="left:130px;top:685px;height:219px"></div>
  <div class="label" style="left:148px;top:766px">Splash</div>

  <div class="rule" style="left:453px;top:760px;height:232px"></div>
  <div class="label" style="left:471px;top:876px">Login</div>

  <div class="rule" style="left:781px;top:680px;height:240px"></div>
  <div class="label" style="left:800px;top:778px">Signup 01</div>

  <div class="rule" style="left:1098px;top:444px;height:272px"></div>
  <div class="label" style="left:1113px;top:492px">Signup 02</div>

</body>
</html>
```